Cafe menu flyer design

I need if possible A4 double sided menus. Two exemplars: first will contain breakfast menu on one side & refreshments menu on the other side, second exemplar will contain lunch menu on one side & refreshments menu on the other side. We do not need a description of the cafe or any history on these flyers, but design should reflect our surroundings and activities this area. We are located in main ski resort in UK-Cairngorm Mountains, right on the main ski road. The slopes are only 2 miles away from us. We are also very popular with wild life enthusiasts. Continues in design brief!

```html
<!DOCTYPE html>
<html lang="en">
<head>
<meta charset="utf-8">
<title>Fiona's at Ardlarach Cafe – Menu</title>
<link rel="stylesheet" href="https://fonts.googleapis.com/css2?family=Sansita:ital,wght@1,700;1,800&family=Kurale&display=swap">
<style>
  :root {
    --frame-red: #d42a22;
    --frame-cyan: #7fd8ea;
    --title-red: #c0321f;
    --heading-brown: #8e2b1a;
    --ink: #1f1a16;
    --board: #e3e2d6;
    --card: rgba(255,255,255,0.86);
    --band: #f6f6f3;
    --hill-light: #4f8fd0;
    --hill-dark: #101a2c;
  }
  * { box-sizing: border-box; margin: 0; padding: 0; }
  html, body { width: 1200px; height: 850px; overflow: hidden; background: #fff; }
  body { font-family: "Kurale", Georgia, serif; color: var(--ink); }

  .sheet {
    position: relative; width: 1200px; height: 850px;
    background: #fff;
    border: 7px solid var(--frame-red);
  }
  .sheet::after {
    content: ""; position: absolute; inset: 4px;
    border: 2px solid var(--frame-cyan); pointer-events: none;
  }

  .page {
    position: absolute; top: 11px; width: 580px; height: 815px;
    background: var(--board); overflow: hidden;
  }
  .page--front { left: 11px; }
  .page--back { left: 595px; }

  .page__header {
    position: absolute; left: 0; top: 0; width: 100%; height: 108px;
    background: var(--band);
    display: flex; align-items: center; justify-content: center;
  }
  .cafe-name {
    font-family: "Sansita", Georgia, serif; font-style: italic; font-weight: 800;
    font-size: 44px; color: var(--title-red); letter-spacing: 0.3px; margin-top: 8px;
  }

  .menu-card {
    position: absolute; background: var(--card); padding: 6px 8px 8px 8px;
  }
  .menu-card__title {
    font-family: "Sansita", Georgia, serif; font-style: italic; font-weight: 700;
    font-size: 25px; color: var(--heading-brown); line-height: 1.2;
  }

  .item { display: flex; align-items: baseline; white-space: nowrap; }
  .item__dots { flex: 1; border-bottom: 1px dotted #555; margin: 0 6px; transform: translateY(-2px); }
  .item__price { text-align: right; }

  .menu--small .item { font-size: 9.6px; line-height: 14px; }
  .menu--small .item__price { min-width: 38px; }
  .note { font-size: 6.6px; text-transform: uppercase; line-height: 10px; }
  .gap { height: 9px; }

  .menu--large .item { font-size: 15px; line-height: 20.8px; }
  .menu--large .item__price { min-width: 48px; }

  .page-note { position: absolute; font-size: 11px; line-height: 16px; }

  .landscape {
    position: absolute; left: 0; bottom: 0; width: 100%; height: 112px;
    background: linear-gradient(180deg, var(--hill-light) 0%, #2b5a94 35%, #1a2f55 65%, var(--hill-dark) 100%);
  }
</style>
</head>
<body>
<div class="sheet">

  <section class="page page--front">
    <header class="page__header"><h1 class="cafe-name">Fiona’s at Ardlarach Cafe</h1></header>

    <div class="menu-card menu--small" style="left:18px; top:141px; width:539px; height:283px;">
      <h2 class="menu-card__title">Breakfast (9am - 12noon)</h2>
      <div class="item" style="margin-top:3px"><span>Small breakfast (bacon, egg, sausage)</span><span class="item__dots"></span><span class="item__price">£5.50</span></div>
      <div class="item"><span>Large brеakfast ( bacon, egg, sausage, black pudding, potato scone, beans, tomato)</span><span class="item__dots"></span><span class="item__price">£7.95</span></div>
      <div class="note">Both breakfast include tea/cofee/plain hot chocolate &amp; one slice of toast. One free refill drink.</div>
      <div class="gap"></div>
      <div class="item"><span>Pancake breakfast. - Three pancakes served with hot forest berry sauce and maple syrup)</span><span class="item__dots"></span><span class="item__price">£4.95</span></div>
      <div class="note">Add three rashers of bacon for an extra £2.</div>
      <div class="gap"></div>
      <div class="item"><span>Round of toast, served with butter and jam</span><span class="item__dots"></span><span class="item__price">£2.00</span></div>
      <div class="item"><span>Beans on toast</span><span class="item__dots"></span><span class="item__price">£3.50</span></div>
      <div class="item"><span>Beans &amp; egg on toast</span><span class="item__dots"></span><span class="item__price">£4.00</span></div>
      <div class="item"><span>Beans &amp; bacon on toast</span><span class="item__dots"></span><span class="item__price">£4.50</span></div>
      <div class="item"><span>Bacon roll</span><span class="item__dots"></span><span class="item__price">£2.90</span></div>
      <div class="item"><span>Lorne roll</span><span class="item__dots"></span><span class="item__price">£2.50</span></div>
      <div class="item"><span>Black pudding roll</span><span class="item__dots"></span><span class="item__price">£2.50</span></div>
      <div class="item"><span>Fried egg roll</span><span class="item__dots"></span><span class="item__price">£2.00</span></div>
      <div class="item"><span>Any 2 item roll</span><span class="item__dots"></span><span class="item__price">£4.00</span></div>
      <div class="item"><span>Rolls with assorted cold fillings</span><span class="item__dots"></span><span class="item__price">£2.20 - £3.20</span></div>
      <div class="item"><span>Pies (assorted)</span><span class="item__dots"></span><span class="item__price">£2.50</span></div>
    </div>

    <p class="page-note" style="left:36px; top:433px; width:530px;">Gluten free bread, cakes and veggie breakfasts available- for more information, ask staff!<br>At the hight of the season evening meals available. Ask staff for more information.</p>

    <div class="menu-card menu--small" style="left:18px; top:476px; width:539px; height:193px;">
      <h2 class="menu-card__title">Refreshments</h2>
      <div class="item" style="margin-top:2px"><span>Tea</span><span class="item__dots"></span><span class="item__price">£1.50</span></div>
      <div class="item"><span>Filter Coffee, decaf coffee, plain hot chocolate</span><span class="item__dots"></span><span class="item__price">£2.00</span></div>
      <div class="item"><span>Selection of herbal teas</span><span class="item__dots"></span><span class="item__price">£2.00</span></div>
      <div class="item"><span>Specialty strawberry, raspberry, apple &amp; mint tea (black tea with your choice of syrup)</span><span class="item__dots"></span><span class="item__price">£2.50</span></div>
      <div class="item"><span>Assorted premium "Leaf House" teas</span><span class="item__dots"></span><span class="item__price">£2.50</span></div>
      <div class="item"><span>Hot chocolate with cream</span><span class="item__dots"></span><span class="item__price">£2.20</span></div>
      <div class="item"><span>Hot chocolate with marsh mallows</span><span class="item__dots"></span><span class="item__price">£2.20</span></div>
      <div class="item"><span>Hot chocolate with cream &amp; marsh mallows</span><span class="item__dots"></span><span class="item__price">£2.20</span></div>
      <div class="item"><span>Hot chocolate with brandy</span><span class="item__dots"></span><span class="item__price">£3.50</span></div>
      <div class="item"><span>Hot chocolate with brandy, marsh mallows &amp; cream</span><span class="item__dots"></span><span class="item__price">£4.50</span></div>
      <div class="item"><span>Cafe Latte/Cappucino</span><span class="item__dots"></span><span class="item__price">£2.50</span></div>
    </div>

    <p class="page-note" style="left:36px; top:684px;">Refreshments continued on the next side.</p>

    <div class="landscape" role="img" aria-label="Blue mountain range silhouette with a red squirrel holding a nut"></div>
  </section>

  <section class="page page--back">
    <header class="page__header"><h1 class="cafe-name">Fiona’s at Ardlarach Cafe</h1></header>

    <div class="menu-card menu--large" style="left:18px; top:141px; width:539px; height:526px;">
      <h2 class="menu-card__title">Refreshments</h2>
      <div class="item" style="margin-top:2px"><span>Squirrel Latte</span><span class="item__dots"></span><span class="item__price">£3.50</span></div>
      <div class="item"><span>Chocolate Latte</span><span class="item__dots"></span><span class="item__price">£3.50</span></div>
      <div class="item"><span>Cinnamon Latte</span><span class="item__dots"></span><span class="item__price">£3.50</span></div>
      <div class="item"><span>Caramel Latte</span><span class="item__dots"></span><span class="item__price">£3.50</span></div>
      <div class="item"><span>Butterscotch Latte</span><span class="item__dots"></span><span class="item__price">£3.50</span></div>
      <div class="item"><span>Gingerbread Latte</span><span class="item__dots"></span><span class="item__price">£3.50</span></div>
      <div class="item"><span>Mocha</span><span class="item__dots"></span><span class="item__price">£3.50</span></div>
      <div class="item"><span>Glass of milk</span><span class="item__dots"></span><span class="item__price">£1.20</span></div>
      <div class="item"><span>Milkshakes</span><span class="item__dots"></span><span class="item__price">£2.00</span></div>
      <div class="item"><span>Still or Sparkling water</span><span class="item__dots"></span><span class="item__price">£1.80</span></div>
      <div class="item"><span>Cans of juice</span><span class="item__dots"></span><span class="item__price">£1.60</span></div>
      <div class="item"><span>Cartons of juice</span><span class="item__dots"></span><span class="item__price">£1.50</span></div>
      <div class="item"><span>Filter Coffee, decaf coffee, plain hot chocolate</span><span class="item__dots"></span><span class="item__price">£2.00</span></div>
      <div class="item"><span>Selection of herbal teas</span><span class="item__dots"></span><span class="item__price">£2.00</span></div>
      <div class="item"><span>Assorted premium "Leaf House" teas</span><span class="item__dots"></span><span class="item__price">£2.50</span></div>
      <div class="item"><span>Hot chocolate with cream</span><span class="item__dots"></span><span class="item__price">£2.20</span></div>
      <div class="item"><span>Hot chocolate with marsh mallows</span><span class="item__dots"></span><span class="item__price">£2.20</span></div>
      <div class="item"><span>Hot chocolate with cream &amp; marsh mallows</span><span class="item__dots"></span><span class="item__price">£2.20</span></div>
      <div class="item"><span>Hot chocolate with brandy</span><span class="item__dots"></span><span class="item__price">£3.50</span></div>
      <div class="item"><span>Hot chocolate with brandy, marsh mallows &amp; cream</span><span class="item__dots"></span><span class="item__price">£4.50</span></div>
      <div class="item"><span>Cafe Latte/Cappucino</span><span class="item__dots"></span><span class="item__price">£2.50</span></div>
      <div class="item"><span>Specialty strawberry, raspberry, apple &amp; mint tea</span></div>
      <div class="item"><span>(black tea with your choice of syrup)</span><span class="item__dots"></span><span class="item__price">£2.50</span></div>
    </div>

    <div class="landscape" role="img" aria-label="Blue mountain range silhouette with a red squirrel holding a nut"></div>
  </section>

</div>
</body>
</html>
```